jewellery store flyer

Front to show
-company name and logo
underneath of company name, I want " The perfect creation" to be written.
-background bright tone jewellery or model wearing jewellery(prefer engagement and wedder or wedder set)

--------------------------------------------------------------
Back to show list of service and brief map of location
with addresss and contact detail

introducing newly established jewellery store with exclusive and unique jewellery. We offer you
-specialized in hand made jewellery
-on site jeweller and designer
-repair and restoring
-laser engraving and laser solder

5/38 Marrowick Street Griffith ACT 2603
02) 6174 3920
Enquiry: fern.w@postbox.net
---------------------------------------------------------------------
I have enclosed mockups that I made by myself, to show what I was thinking. this is just for reference. New flyer doesn't need to look the same.

I don't mind either holizontal nor vertical.
I don't mind if you add text or remove text that I have written above.
I want flyer to look morden and neat.

Good luck to you & me and enjoy creation.
Kind regards,
Tansy

Target Market(s)

introducing newly established store.
aiming for engagement & wedding rings and remakes

Industry/Entity Type

It Company

Font styles to use
Other font styles liked:
• Monotype corsive for script but name and address for SERIF

Colors

Designer to choose colors to be used in the design.

Requirements
Must have
• background photo including jewellery
• company name and address
• service detail
Nice to have
• brief map of location( I have red circled few places that people know more on the map I attached here.)
• Map to be simplified please.
• Please do not use Google map directly.
• Opening hours: Mon-Fri 9.30 to 5.30 Sat 10.00 to 5

```html
<!DOCTYPE html>
<html lang="en">
<head>
<meta charset="utf-8">
<title>Juniper Jewellery Flyer</title>
<link rel="stylesheet" href="https://fonts.googleapis.com/css2?family=Cinzel:wght@400;700&family=Lato:ital,wght@1,400&display=swap">
<style>
  :root {
    --page: #e4e4e4;
    --white: #ffffff;
    --pink: #ec2e6d;
    --gold-light: #f3d79c;
    --gold: #c99a52;
    --gold-deep: #9e7035;
    --sand: #d9b27a;
  }
  * { margin: 0; padding: 0; box-sizing: border-box; }
  html, body { width: 1200px; height: 1200px; overflow: hidden; }
  body {
    background: radial-gradient(circle at 50% 50%, #f4f4f4 0%, var(--page) 70%, #cfcfcf 100%);
    position: relative;
    font-family: 'Lato', sans-serif;
  }
  .flyer {
    position: absolute;
    left: 229px;
    width: 734px;
    height: 520px;
    overflow: hidden;
    box-shadow: 0 14px 22px rgba(0,0,0,0.22);
  }
  .flyer--front { top: 47px; }
  .flyer--back { top: 605px; }
  .flyer svg.backdrop { position: absolute; inset: 0; }
  .centered { position: absolute; transform: translateX(-50%); white-space: nowrap; text-align: center; }

  .logo-mark {
    position: absolute; left: 526px; top: 23px;
    width: 56px; height: 56px; border-radius: 50%;
    border: 1.5px solid rgba(255,255,255,0.85);
  }
  .logo-name {
    left: 554px; top: 88px;
    font-family: 'Cinzel', serif; font-size: 16px; color: var(--white); letter-spacing: 0.5px;
  }
  .hero-name {
    left: 560px; top: 140px;
    font-family: 'Cinzel', serif; font-weight: 700; font-size: 50px; line-height: 55px;
    color: var(--gold-light);
    background: linear-gradient(180deg, var(--gold-light) 0%, var(--gold) 60%, var(--gold-deep) 100%);
    -webkit-background-clip: text; background-clip: text; -webkit-text-fill-color: transparent;
  }
  .tagline-lead {
    left: 542px; top: 320px;
    font-style: italic; font-size: 33px; color: var(--white);
  }
  .tagline-main {
    left: 542px; top: 358px;
    font-family: 'Cinzel', serif; font-size: 43px; color: var(--white); letter-spacing: 1px;
  }
  .call-label, .call-number { left: 172px; font-family: 'Cinzel', serif; color: var(--white); }
  .call-label { top: 436px; font-size: 25px; letter-spacing: 1px; }
  .call-number { top: 463px; font-size: 29px; font-weight: 700; }

  .back-title {
    left: 514px; top: 40px;
    font-family: 'Cinzel', serif; font-size: 40px; color: var(--white);
  }
  .services { position: absolute; left: 370px; top: 116px; width: 310px; list-style: none; }
  .services li {
    height: 46px; display: flex; align-items: center; justify-content: center;
    font-style: italic; font-size: 22px; color: var(--white); white-space: nowrap;
  }
  .services li + li { border-top: 2px solid rgba(255,255,255,0.9); }
  .contact { left: 524px; font-style: italic; font-size: 12px; line-height: 14px; color: var(--white); }
  .contact--address { top: 468px; }
  .contact--reach { top: 483px; }
  .contact--hours { top: 498px; }
</style>
</head>
<body>

<section class="flyer flyer--front">
  <svg class="backdrop" width="734" height="520" viewBox="0 0 734 520">
    <defs>
      <linearGradient id="frontPurple" x1="0" y1="0" x2="1" y2="1">
        <stop offset="0" stop-color="#5a1a5e"/>
        <stop offset="0.5" stop-color="#7a2378"/>
        <stop offset="1" stop-color="#3f1246"/>
      </linearGradient>
      <radialGradient id="frontMagenta" cx="0.6" cy="0.35" r="0.8">
        <stop offset="0" stop-color="#d8205f"/>
        <stop offset="1" stop-color="#8d1450"/>
      </radialGradient>
      <radialGradient id="ringPhoto" cx="0.5" cy="0.45" r="0.6">
        <stop offset="0" stop-color="#e2dde2"/>
        <stop offset="0.35" stop-color="#b52a5a"/>
        <stop offset="1" stop-color="#8a1840"/>
      </radialGradient>
    </defs>
    <rect width="734" height="520" fill="url(#frontPurple)"/>
    <path d="M300 0 Q170 330 352 520 L734 520 L734 0 Z" fill="var(--white)"/>
    <path d="M318 0 Q190 330 372 520 L734 520 L734 0 Z" fill="var(--pink)"/>
    <path d="M335 0 Q210 330 390 520 L734 520 L734 0 Z" fill="url(#frontMagenta)"/>
    <path d="M734 390 Q700 490 610 520 L734 520 Z" fill="#e9e6ea"/>
    <circle cx="183" cy="249" r="171" fill="rgba(255,255,255,0.18)" stroke="var(--white)" stroke-width="2"/>
    <circle cx="183" cy="249" r="157" fill="url(#ringPhoto)" role="img" aria-label="Photo of a diamond solitaire engagement ring on red silk"/>
    <line x1="388" y1="283" x2="705" y2="283" stroke="var(--white)" stroke-width="2"/>
    <circle cx="546" cy="283" r="3" fill="var(--white)"/>
  </svg>
  <div class="logo-mark"></div>
  <div class="centered logo-name">JUNIPER JEWELLERY</div>
  <div class="centered hero-name">JUNIPER<br>JEWELLERY</div>
  <div class="centered tagline-lead">The perfect</div>
  <div class="centered tagline-main">CREATION</div>
  <div class="centered call-label">CALL US TODAY</div>
  <div class="centered call-number">(02) 6174 3920</div>
</section>

<section class="flyer flyer--back">
  <svg class="backdrop" width="734" height="520" viewBox="0 0 734 520">
    <defs>
      <radialGradient id="backMagenta" cx="0.6" cy="0.3" r="0.9">
        <stop offset="0" stop-color="#d81f5e"/>
        <stop offset="1" stop-color="#991550"/>
      </radialGradient>
      <linearGradient id="portrait" x1="0" y1="0" x2="1" y2="1">
        <stop offset="0" stop-color="#7a4a30"/>
        <stop offset="0.45" stop-color="#e6bfa8"/>
        <stop offset="1" stop-color="#f4dccd"/>
      </linearGradient>
      <linearGradient id="goldBand" x1="0" y1="0" x2="1" y2="0">
        <stop offset="0" stop-color="#e0bb84"/>
        <stop offset="0.5" stop-color="var(--gold)"/>
        <stop offset="1" stop-color="#e2c08c"/>
      </linearGradient>
      <radialGradient id="mapArea" cx="0.5" cy="0.5" r="0.6">
        <stop offset="0" stop-color="#f2efe8"/>
        <stop offset="1" stop-color="#dcd8cf"/>
      </radialGradient>
    </defs>
    <rect width="734" height="520" fill="url(#backMagenta)"/>
    <path d="M210 400 C330 330 520 390 734 395 L734 520 L210 520 Z" fill="var(--white)"/>
    <path d="M215 415 C335 350 520 410 734 412 L734 520 L215 520 Z" fill="url(#goldBand)"/>
    <path d="M0 0 L318 0 C300 120 310 300 250 390 C230 430 210 470 200 520 L0 520 Z" fill="url(#portrait)" role="img" aria-label="Portrait photo of a woman wearing long diamond drop earrings"/>
    <circle cx="524" cy="378" r="84" fill="var(--sand)"/>
    <circle cx="524" cy="378" r="78" fill="url(#mapArea)" role="img" aria-label="Simplified street map of Griffith shops with the store location marked"/>
  </svg>
  <div class="centered back-title">Juniper Jewellery</div>
  <ul class="services">
    <li>specialized in hand made jewellery</li>
    <li>on site jeweller and designer</li>
    <li>repair and restoring</li>
    <li>laser engraving and laser solder</li>
  </ul>
  <div class="centered contact contact--address">5/38 Marrowick Street Griffith ACT 2603</div>
  <div class="centered contact contact--reach">(02) 6174 3920 &nbsp;·&nbsp; Enquiry: fern.w@postbox.net</div>
  <div class="centered contact contact--hours">Mon–Fri 9.30 to 5.30 &nbsp;·&nbsp; Sat 10.00 to 5</div>
</section>

</body>
</html>
```